Venture capital website it shall be called Loram Ventures

Venture capital Name is : Loram Ventures

i have already regesieted a website and comunicate the details with you when i choose a design.

i need a simple website design for a newly established venture capital. i would like something similar to the websites listed down:

http://www.tovelpark.com/

http://www.brisoltidefunds.com/

https://kpdrift.com/

http://www.mullenfield.com/

i like mullen field the most

Target Market(s)

entrepreneur - startups

Industry/Entity Type

Venture Capital

Number of Pages Required

4 page

Font styles to use
Serif
Sans Serif

Colors
ffc214
fece3e

Requirements
Must have
• the following sections:
• Philosophy (about loram Ventures)
• Team
• Knowledge
• address - contact
Nice to have
• http://www.tovelpark.com/
• http://www.brisoltidefunds.com/
• https://kpdrift.com/
• http://www.mullenfield.com/

```html
<!DOCTYPE html>
<html lang="en">
<head>
<meta charset="utf-8">
<title>Loram Ventures</title>
<link href="https://fonts.googleapis.com/css2?family=Open+Sans:wght@400;600;700;800&display=swap" rel="stylesheet">
<style>
:root{
  --yellow:#ffc214;
  --yellow-soft:#fece3e;
  --gold-dark:#b09a1c;
  --ink:#222222;
  --text:#555555;
  --muted:#f7f7f7;
  --line:#bdbdbd;
  --dark:#3b3a36;
  --dark-2:#2f2e2b;
  --white:#ffffff;
}
*{margin:0;padding:0;box-sizing:border-box}
html,body{width:1200px;height:3152px;overflow:hidden}
body{font-family:"Open Sans",Arial,sans-serif;color:var(--text);background:var(--white);position:relative}
section,header{position:absolute;left:0;width:1200px}
.abs{position:absolute}
.center{text-align:center;left:0;width:1200px}

/* hero */
.hero{top:0;height:553px}
.hero-bg{position:absolute;inset:0;background:linear-gradient(180deg,#1d2333 0%,#2a3146 45%,#5a4a3a 75%,#2a2520 100%)}
.brand{left:99px;top:34px;color:var(--white);font-weight:700;font-size:36px;letter-spacing:4px}
.nav{right:108px;top:44px;display:flex;gap:40px;align-items:center}
.nav a{color:var(--white);font-weight:700;font-size:16px;text-decoration:none}
.nav a.active{color:var(--yellow)}
.hero-title{top:170px;color:var(--white);font-weight:800;font-size:76px;letter-spacing:1px}
.hero-sub{top:274px;color:var(--white);font-weight:600;font-size:28px}
.hero-btn{left:514px;top:336px;width:172px;height:50px;border:2px solid var(--white);border-radius:25px;color:var(--white);font-weight:700;font-size:16px;line-height:46px;text-align:center}
.dots{left:566px;top:478px;display:flex;gap:6px}
.dots span{width:13px;height:13px;border:2px solid var(--white);border-radius:50%}
.dots span.on{background:var(--white)}

.pointer-down{left:571px;top:553px;width:0;height:0;border-left:29px solid transparent;border-right:29px solid transparent;border-top:30px solid var(--gold-dark);z-index:2}

h2{font-weight:700;font-size:34px;color:var(--ink);text-align:center;letter-spacing:.5px}

/* philosophy */
.philosophy{top:553px;height:529px;background:var(--white)}
.philosophy h2{position:absolute;top:100px;width:100%}
.philosophy-text{left:230px;width:740px;top:180px;text-align:center;font-size:15px;line-height:27px}
.philosophy-text p{margin-bottom:26px}

/* team */
.team{top:1082px;height:820px;background:var(--muted);border-top:1px solid #e8e8e8}
.team h2{position:absolute;top:83px;width:100%}
.member{top:152px;width:500px;text-align:center}
.member.one{left:78px}
.member.two{left:616px}
.photo{width:298px;height:298px;border-radius:50%;margin:0 auto;border:6px solid var(--white);box-shadow:0 0 0 1px #ddd;background:linear-gradient(160deg,#cfd3d6,#eeeeec 60%,#b9b2a8)}
.member h3{margin-top:48px;font-size:22px;font-weight:700;color:var(--ink);letter-spacing:.5px}
.member p{margin:22px auto 0;width:450px;font-size:14px;line-height:29px}
.member-social{margin-top:30px;display:flex;justify-content:center;gap:14px}
.member-social span{width:40px;height:40px;border-radius:50%;background:#333}

/* knowledge */
.knowledge{top:1902px;height:645px;background:var(--white)}
.knowledge h2{position:absolute;top:106px;width:100%}
.knowledge-sub{top:178px;color:var(--yellow);font-size:20px;font-weight:600}
.value{width:240px;text-align:center}
.value .ring{width:168px;height:168px;border:2px solid var(--line);border-radius:50%;margin:0 auto;display:flex;align-items:center;justify-content:center;background:var(--white)}
.value.big .ring{width:214px;height:214px;border:none;background:var(--yellow)}
.value h4{font-size:20px;font-weight:600;color:var(--ink);line-height:28px;margin-top:24px}
.value.big h4{margin-top:22px}

/* contact */
.contact{top:2547px;height:605px;background:var(--dark)}
.pointer-up{left:571px;top:-30px;width:0;height:0;border-left:29px solid transparent;border-right:29px solid transparent;border-bottom:30px solid var(--gold-dark)}
.contact h2{position:absolute;top:76px;width:100%;color:var(--white);font-size:36px}
.contact h5{font-size:15px;font-weight:700;color:var(--white);letter-spacing:.3px}
.form{left:99px;top:160px;width:630px}
.field-label{font-size:11px;color:var(--white);display:block;margin-bottom:6px}
.input{background:var(--white);height:32px;border:1px solid #ccc}
.row{display:flex;gap:8px;margin-top:24px}
.row>div{flex:1}
.block{margin-top:14px}
.textarea{height:78px}
.submit{left:531px;top:454px;width:99px;height:34px;border-radius:17px;background:var(--yellow);color:var(--white);font-size:14px;font-weight:700;text-align:center;line-height:34px}
.info{left:809px;top:160px;width:300px}
.info-item{display:flex;align-items:flex-start;gap:24px;margin-top:26px;color:var(--white);font-size:14px;line-height:24px}
.info-item .ico{width:38px;height:38px;flex:none;border:2px solid #777;border-radius:50%;display:flex;align-items:center;justify-content:center}
.social{left:809px;top:400px}
.social-row{display:flex;gap:6px;margin-top:20px}
.social-row span{width:28px;height:28px;border-radius:50%;background:#8a8a86}
.divider{left:99px;top:525px;width:1002px;height:1px;background:#55544f}
.copyright{top:557px;color:var(--white);font-size:13px}
</style>
</head>
<body>

<header class="hero">
  <div class="hero-bg" role="img" aria-label="Night city skyline with light trails on a highway"></div>
  <div class="abs brand">LORAM</div>
  <nav class="abs nav">
    <a class="active" href="#">HOME</a>
    <a href="#">PHILOSOPHY</a>
    <a href="#">TEAM</a>
    <a href="#">KNOWLEDGE</a>
    <a href="#">CONTACT</a>
    <svg width="18" height="18" viewBox="0 0 18 18"><circle cx="7.5" cy="7.5" r="5.5" fill="none" stroke="#fff" stroke-width="2.4"/><line x1="11.5" y1="11.5" x2="16.5" y2="16.5" stroke="#fff" stroke-width="2.6" stroke-linecap="round"/></svg>
  </nav>
  <div class="abs center hero-title">LORAM VENTURES</div>
  <div class="abs center hero-sub">We are a new Venture Capital company in Kuwait</div>
  <div class="abs hero-btn">GET MORE INFO</div>
  <div class="abs dots"><span class="on"></span><span></span><span></span><span></span></div>
</header>

<div class="abs pointer-down"></div>

<section class="philosophy">
  <h2>PHILOSOPHY</h2>
  <div class="abs philosophy-text">
    <p>To create a pioneering business model that leads Loram Venture Capital to be amongst the industry leaders in the regional venture capital market.</p>
    <p>To establish strategic partnerships with underserved SME's in the GCC and the MENA regions that will result in their expansion, growth, development and higher profitability.</p>
    <p>To become leading Venture Capital in Kuwait and motivating businesses to achieve growth. To bridge the gap between private equity market and the public. To maximize investors' return through professional planning and providing a new prosper direction to the private equity industry.</p>
  </div>
</section>

<section class="team">
  <h2>TEAM</h2>
  <div class="abs member one">
    <div class="photo" role="img" aria-label="Portrait of Rashed Al Nouri"></div>
    <h3>RASHED AL NOURI</h3>
    <p>Rashed Al Nouri holds a BA degree in Mass Media from Kuwait University. Al Nouri is Founder &amp; General Manager of Nadeem, the leading Social Media Agency in Kuwait &amp; the GCC. Nadeem was the first agency of its sort in the region.</p>
    <div class="member-social"><span></span><span></span><span></span></div>
  </div>
  <div class="abs member two">
    <div class="photo" role="img" aria-label="Portrait of Faisal Yousef Al-Hamdan"></div>
    <h3>FAISAL YOUSEF AL-HAMDAN</h3>
    <p>Faisal Yousef Al-Hamdan holds a BA degree in Finance from Kuwait University. He has vast knowledge and skills in areas such as merger and acquisition, business strategy, financial analysis, evaluating business opportunities, and evaluating companies in different sectors.</p>
    <div class="member-social"><span></span><span></span><span></span></div>
  </div>
</section>

<section class="knowledge">
  <h2>KNOWLEDGE</h2>
  <div class="abs center knowledge-sub">The foundation of LVC values laid on following principles</div>

  <div class="abs value" style="left:61px;top:267px">
    <div class="ring"><svg width="64" height="64" viewBox="0 0 64 64" fill="var(--yellow)"><circle cx="22" cy="36" r="14"/><circle cx="22" cy="36" r="5" fill="#fff"/><g stroke="var(--yellow)" stroke-width="7"><line x1="22" y1="16" x2="22" y2="56"/><line x1="2" y1="36" x2="42" y2="36"/><line x1="8" y1="22" x2="36" y2="50"/><line x1="36" y1="22" x2="8" y2="50"/></g><circle cx="22" cy="36" r="5" fill="#fff"/><circle cx="47" cy="17" r="9"/><circle cx="47" cy="17" r="3.5" fill="#fff"/><circle cx="48" cy="46" r="7"/><circle cx="48" cy="46" r="2.8" fill="#fff"/></svg></div>
    <h4>Collective<br>Performance</h4>
  </div>
  <div class="abs value" style="left:271px;top:267px">
    <div class="ring"><svg width="52" height="64" viewBox="0 0 52 64" fill="none" stroke="var(--yellow)" stroke-width="4"><path d="M26 4a19 19 0 0 0-11 34c3 3 4 6 4 10h14c0-4 1-7 4-10A19 19 0 0 0 26 4z"/><line x1="19" y1="54" x2="33" y2="54"/><line x1="21" y1="60" x2="31" y2="60"/></svg></div>
    <h4>Innovation</h4>
  </div>
  <div class="abs value big" style="left:477px;top:244px">
    <div class="ring"><svg width="76" height="62" viewBox="0 0 76 62" fill="none" stroke="#fff" stroke-width="4"><polyline points="4,2 4,58 74,58"/><polyline points="12,48 30,28 42,38 66,14"/><polyline points="54,12 68,12 68,26"/></svg></div>
    <h4>Client-Centric<br>Approach</h4>
  </div>
  <div class="abs value" style="left:687px;top:267px">
    <div class="ring"><svg width="68" height="56" viewBox="0 0 68 56" fill="var(--yellow)"><circle cx="34" cy="14" r="10"/><circle cx="14" cy="18" r="8"/><circle cx="54" cy="18" r="8"/><path d="M18 50c0-12 7-20 16-20s16 8 16 20z"/><path d="M0 46c0-9 5-16 14-16 4 0 6 1 8 3-4 4-6 9-6 13z"/><path d="M68 46c0-9-5-16-14-16-4 0-6 1-8 3 4 4 6 9 6 13z"/></svg></div>
    <h4>Teamwork</h4>
  </div>
  <div class="abs value" style="left:895px;top:267px">
    <div class="ring"><svg width="46" height="60" viewBox="0 0 46 60"><path d="M0 0h30l16 16v44H0z" fill="var(--yellow)"/><path d="M30 0v16h16z" fill="#fde59a"/><g stroke="#fff" stroke-width="3"><line x1="10" y1="28" x2="36" y2="28"/><line x1="10" y1="37" x2="36" y2="37"/><line x1="10" y1="46" x2="36" y2="46"/></g></svg></div>
    <h4>Comply with rules<br>and regulations</h4>
  </div>
</section>

<section class="contact">
  <div class="abs pointer-up"></div>
  <h2>CONTACT US</h2>

  <div class="abs form">
    <h5>CONTACT FORM</h5>
    <div class="row">
      <div><span class="field-label">NAME :</span><div class="input"></div></div>
      <div><span class="field-label">PHONE NO :</span><div class="input"></div></div>
    </div>
    <div class="block"><span class="field-label">EMAIL :</span><div class="input"></div></div>
    <div class="block"><span class="field-label">MESSAGE :</span><div class="input textarea"></div></div>
  </div>
  <div class="abs submit" style="left:630px">SUBMIT</div>

  <div class="abs info">
    <h5>CONTACT INFORMATION</h5>
    <div class="info-item">
      <span class="ico"><svg width="14" height="18" viewBox="0 0 14 18"><path d="M7 0a7 7 0 0 0-7 7c0 5 7 11 7 11s7-6 7-11a7 7 0 0 0-7-7z" fill="var(--yellow)"/><circle cx="7" cy="7" r="2.5" fill="var(--dark)"/></svg></span>
      <span>2710 Harbor Lane, Suite 300<br>Westfield CA 90417</span>
    </div>
    <div class="info-item" style="margin-top:14px">
      <span class="ico"><svg width="16" height="12" viewBox="0 0 16 12"><rect width="16" height="12" rx="1" fill="var(--yellow)"/><polyline points="0,1 8,7 16,1" fill="none" stroke="var(--dark)" stroke-width="1.5"/></svg></span>
      <span style="padding-top:6px">GP@loramvc.com</span>
    </div>
    <div class="info-item" style="margin-top:18px">
      <span class="ico"><svg width="16" height="16" viewBox="0 0 16 16"><path d="M3 1l3 3-2 2c1 2 4 5 6 6l2-2 3 3-2 2C7 15 1 9 1 3z" fill="var(--yellow)"/></svg></span>
      <span style="padding-top:6px">+965 5550-0142</span>
    </div>
  </div>

  <div class="abs social">
    <h5>SOCIAL MEDIA</h5>
    <div class="social-row"><span></span><span></span><span></span><span></span><span></span><span></span></div>
  </div>

  <div class="abs divider"></div>
  <div class="abs center copyright">Copyright © 2017, Loram Ventures. All Rights Reserved.</div>
</section>

</body>
</html>
```